Funeral Services Site

We need a website for a Funeral Services company. The old website is: www.rouwcentrumdelvoort.be We need the same structure and text.

Target Market(s)

Customers.

Coding

Coded - Design and coding required

Number of Pages Required

4 page

Font styles to use
Serif
Sans Serif
Script

```html
<!DOCTYPE html>
<html lang="en">
<head>
<meta charset="utf-8">
<title>Condole Online – Funeral home Delvoort bvba</title>
<link rel="stylesheet" href="https://fonts.googleapis.com/css2?family=Tinos:wght@400;700&family=Jost:wght@400;500&family=Playball&display=swap">
<style>
:root{
  --gold:#b8860b;
  --dark:#2e2e2e;
  --ink:#222;
  --text:#555;
  --line:#d9d9d9;
  --field:#dcdcdc;
  --foot-bar:#e8e8e8;
}
*{box-sizing:border-box;margin:0;padding:0}
html,body{width:1200px;height:3979px;overflow:hidden}
body{position:relative;background:#fff;font-family:"Jost",sans-serif;color:var(--text)}

.topbar{position:absolute;top:0;left:0;width:1200px;height:42px;background:var(--dark);color:#eee;font-size:13px}
.topbar .item{position:absolute;top:12px;display:flex;align-items:center;gap:8px}
.topbar .lang{position:absolute;left:1002px;top:6px;width:57px;height:30px;background:#fff;color:var(--gold);font-size:12px;display:flex;align-items:center;justify-content:center}

.header{position:absolute;top:42px;left:0;width:1200px;height:100px;background:#fff;border-bottom:1px solid #eee}
.brand{position:absolute;left:142px;top:22px;display:flex;align-items:center;gap:10px;font-family:"Tinos",serif;font-weight:700;color:var(--ink)}
.brand .dot{width:56px;height:56px;border-radius:50%;background:var(--ink)}
.brand .name{font-size:24px;line-height:24px}
.brand small{font-size:16px}
.nav a{position:absolute;top:0;height:100px;line-height:124px;font-family:"Tinos",serif;font-weight:700;font-size:14px;color:var(--ink);text-decoration:none}
.nav a.active{background:#f4f4f4;color:var(--gold);border-bottom:2px solid var(--gold);padding:0 14px}

.hero{position:absolute;top:142px;left:0;width:1200px;height:386px;background:linear-gradient(90deg,#141414 0%,#2a2a2a 38%,#6e7a5a 58%,#c9d6a4 75%,#eef1d6 88%,#9fb06a 100%)}
.hero h1{position:absolute;left:142px;top:88px;font-family:"Playball",cursive;font-weight:400;font-size:52px;line-height:68px;color:#fff}
.btn-outline-light{position:absolute;left:142px;top:244px;width:173px;height:43px;border:2px solid #fff;color:#fff;font-family:"Tinos",serif;font-weight:700;font-size:16px;display:flex;align-items:center;justify-content:center}

.intro{position:absolute;top:604px;left:141px;width:918px;text-align:center}
.intro h2{font-family:"Tinos",serif;font-weight:700;font-size:28px;color:var(--ink)}
.intro p{margin-top:14px;font-size:13px;line-height:22px}

.card{position:absolute;left:141px;width:918px;height:224px;border:1px solid var(--line)}
.card .photo{position:absolute;left:23px;top:18px;width:190px;height:189px}
.card .info{position:absolute;left:249px;top:34px;width:280px;text-align:center}
.card .info h3{font-family:"Tinos",serif;font-weight:700;font-size:18px;color:var(--ink);white-space:nowrap}
.card .info .dates{font-size:14px;margin-top:5px}
.btn-gold{display:flex;align-items:center;justify-content:center;border:2px solid var(--gold);color:var(--gold);font-family:"Tinos",serif;font-weight:700;font-size:13px;margin:0 auto}
.card .download{width:176px;height:37px;margin-top:12px}
.card .flowers{width:122px;height:37px;margin-top:13px}
.card .form{position:absolute;left:565px;top:18px;width:329px}
.field{border:1px solid var(--field);height:29px;font-size:11px;padding:7px 12px;color:#666;margin-bottom:8px}
.field.area{height:66px}
.card .send{width:72px;height:31px;margin:9px 0 0 0;font-size:14px}

.load-more{position:absolute;left:548px;top:3275px;width:104px;height:40px;font-size:14px}

.cta{position:absolute;top:3400px;left:0;width:1200px;height:280px;background:linear-gradient(180deg,#1c1c1c,#2a2622 55%,#3a2420);text-align:center;color:#fff}
.cta h2{position:absolute;top:80px;left:0;width:1200px;font-family:"Tinos",serif;font-weight:700;font-size:20px;line-height:30px}
.cta .call{position:absolute;left:442px;top:168px;font-family:"Tinos",serif;font-weight:700;font-size:14px}
.cta .btn-gold{position:absolute;left:608px;top:159px;width:147px;height:36px}

.footer{position:absolute;top:3680px;left:0;width:1200px;height:267px;background:#fff}
.footer h4{font-family:"Tinos",serif;font-weight:700;font-size:14px;color:var(--ink);position:absolute;top:58px}
.footer ul{list-style:none;position:absolute;top:82px;font-size:12px}
.footer .links li{height:25px}
.footer .links li::before{content:"»";margin-right:10px;color:#888}
.footer .contact li{display:flex;gap:12px;line-height:18px;margin-bottom:8px}
.footer .map{position:absolute;left:596px;top:83px;width:205px;height:109px;background:linear-gradient(135deg,#eceae4,#dfe4ea 60%,#e7e3dc)}
.footer .brand{left:865px;top:92px}
.footer .brand .dot{width:48px;height:48px}
.footer .brand .name{font-size:18px;line-height:18px}
.footer .brand small{font-size:13px}
.social{position:absolute;top:146px;left:905px;display:flex;gap:10px}
.social span{width:19px;height:19px;display:block}
.bottombar{position:absolute;top:3947px;left:0;width:1200px;height:32px;background:var(--foot-bar);font-size:12px;color:#444}
.bottombar .l{position:absolute;left:142px;top:9px}
.bottombar .r{position:absolute;right:141px;top:9px}
</style>
</head>
<body>

<div class="topbar">
  <div class="item" style="left:142px">
    <svg width="18" height="18" viewBox="0 0 24 24" fill="none" stroke="#eee" stroke-width="1.6"><path d="M5 3h4l2 5-2.5 1.5a11 11 0 0 0 6 6L16 13l5 2v4a2 2 0 0 1-2 2A16 16 0 0 1 3 5a2 2 0 0 1 2-2z"/></svg>
    <span style="font-size:14px">011 23 45 67</span>
  </div>
  <div class="item" style="left:287px">
    <svg width="18" height="14" viewBox="0 0 24 18" fill="none" stroke="#eee" stroke-width="1.6"><rect x="1" y="1" width="22" height="16"/><path d="M1 1l11 9 11-9"/></svg>
    <span style="font-size:12px">mourningcenter.delvoort@example.com</span>
  </div>
  <div class="lang">EN ▾</div>
</div>

<header class="header">
  <div class="brand"><span class="dot"></span><div class="name">Funeral home<br>Delvoort <small>bvba</small></div></div>
  <nav class="nav">
    <a style="left:571px">Home</a>
    <a style="left:648px">About us</a>
    <a class="active" style="left:732px">Condole online</a>
    <a style="left:878px">Order flowers</a>
    <a style="left:1007px">Contact</a>
  </nav>
</header>

<section class="hero" role="img" aria-label="Photo of white roses and green flowers beside a dark wooden surface">
  <h1>A Personal Service In<br>Farewell Guidance</h1>
  <div class="btn-outline-light">Contact Us Today</div>
</section>

<section class="intro">
  <h2>Condole Online</h2>
  <p>Do you want to leave nice words to the family of a deceased person? Funeral home Delvoort gives you the opportunity to convey your message quickly and<br>discreetly . Here you can condole the family of every deceased person online .</p>
</section>

<div class="card" style="top:721px">
  <div class="photo" role="img" aria-label="Portrait photo of the deceased" style="background:linear-gradient(160deg,#5d6b4a,#b9aba2 60%,#d8c6cc)"></div>
  <div class="info"><h3>Hilde Wouters</h3><div class="dates">March 12, 1951 - May 6, 2019</div><div class="btn-gold download">Download Funeral letter</div><div class="btn-gold flowers">Order Flowers</div></div>
  <div class="form"><div class="field">Hilde Wouters</div><div class="field">Your name*</div><div class="field area">Leave a message*</div><div class="btn-gold send">Send</div></div>
</div>

<div class="card" style="top:976px">
  <div class="photo" role="img" aria-label="Portrait photo of the deceased" style="background:linear-gradient(160deg,#6a4a35,#a88672 55%,#ddd)"></div>
  <div class="info"><h3>Frederik Albert Janssens</h3><div class="dates">January 18, 1933 - May 3, 2019</div><div class="btn-gold download">Download Funeral letter</div><div class="btn-gold flowers">Order Flowers</div></div>
  <div class="form"><div class="field">Frederik Albert Janssens</div><div class="field">Your name*</div><div class="field area">Leave a message*</div><div class="btn-gold send">Send</div></div>
</div>

<div class="card" style="top:1231px">
  <div class="photo" role="img" aria-label="Portrait photo of the deceased" style="background:linear-gradient(160deg,#f4f4f2,#d9c9ad 55%,#8e8e78)"></div>
  <div class="info"><h3>Rita Moens</h3><div class="dates">August 11, 1938 - April 30, 2019</div><div class="btn-gold download">Download Funeral letter</div><div class="btn-gold flowers">Order Flowers</div></div>
  <div class="form"><div class="field">Rita Moens</div><div class="field">Your name*</div><div class="field area">Leave a message*</div><div class="btn-gold send">Send</div></div>
</div>

<div class="card" style="top:1486px">
  <div class="photo" role="img" aria-label="Portrait photo of the deceased" style="background:linear-gradient(160deg,#4a3a2a,#c7b39f 50%,#c29a2e)"></div>
  <div class="info"><h3>Godelieve Roels</h3><div class="dates">November 4, 1928 - April 27, 2019</div><div class="btn-gold download">Download Funeral letter</div><div class="btn-gold flowers">Order Flowers</div></div>
  <div class="form"><div class="field">Godelieve Roels</div><div class="field">Your name*</div><div class="field area">Leave a message*</div><div class="btn-gold send">Send</div></div>
</div>

<div class="card" style="top:1741px">
  <div class="photo" role="img" aria-label="Portrait photo of the deceased" style="background:linear-gradient(160deg,#fafafa,#d8b8a4 55%,#2a3550)"></div>
  <div class="info"><h3>Marcel Geerts</h3><div class="dates">October 2, 1937 - April 25, 2019</div><div class="btn-gold download">Download Funeral letter</div><div class="btn-gold flowers">Order Flowers</div></div>
  <div class="form"><div class="field">Marcel Geerts</div><div class="field">Your name*</div><div class="field area">Leave a message*</div><div class="btn-gold send">Send</div></div>
</div>

<div class="card" style="top:1996px">
  <div class="photo" role="img" aria-label="Photo of the deceased beside a red motorcycle" style="background:linear-gradient(160deg,#4d6b3a,#6b6b6b 50%,#9b1c22)"></div>
  <div class="info"><h3>Walter "Wally" Hendrickx</h3><div class="dates">March 14, 1962 - April 22, 2019</div><div class="btn-gold download">Download Funeral letter</div><div class="btn-gold flowers">Order Flowers</div></div>
  <div class="form"><div class="field">Walter "Wally" Hendrickx</div><div class="field">Your name*</div><div class="field area">Leave a message*</div><div class="btn-gold send">Send</div></div>
</div>

<div class="card" style="top:2251px">
  <div class="photo" role="img" aria-label="Black and white portrait photo of the deceased" style="background:linear-gradient(160deg,#555,#bdbdbd 55%,#e4e4e4)"></div>
  <div class="info"><h3>Sofie Lambrechts</h3><div class="dates">November 30, 1994 - April 19, 2019</div><div class="btn-gold download">Download Funeral letter</div><div class="btn-gold flowers">Order Flowers</div></div>
  <div class="form"><div class="field">Sofie Lambrechts</div><div class="field">Your name*</div><div class="field area">Leave a message*</div><div class="btn-gold send">Send</div></div>
</div>

<div class="card" style="top:2506px">
  <div class="photo" role="img" aria-label="Portrait photo of the deceased" style="background:linear-gradient(160deg,#f2f2f2,#c9a998 55%,#3e8a99)"></div>
  <div class="info"><h3>Irma Coenen</h3><div class="dates">September 7, 1935 - April 15, 2019</div><div class="btn-gold download">Download Funeral letter</div><div class="btn-gold flowers">Order Flowers</div></div>
  <div class="form"><div class="field">Irma Coenen</div><div class="field">Your name*</div><div class="field area">Leave a message*</div><div class="btn-gold send">Send</div></div>
</div>

<div class="card" style="top:2761px">
  <div class="photo" role="img" aria-label="Portrait photo of the deceased" style="background:linear-gradient(160deg,#2a2a2a,#b08270 45%,#8fc0c8)"></div>
  <div class="info"><h3>Josephina (Fien) Janssens</h3><div class="dates">February 3, 1931 - April 13, 2019</div><div class="btn-gold download">Download Funeral letter</div><div class="btn-gold flowers">Order Flowers</div></div>
  <div class="form"><div class="field">Josephina (Fien) Janssens</div><div class="field">Your name*</div><div class="field area">Leave a message*</div><div class="btn-gold send">Send</div></div>
</div>

<div class="card" style="top:3016px">
  <div class="photo" role="img" aria-label="Black and white portrait photo of the deceased outdoors" style="background:linear-gradient(160deg,#8a8a8a,#d2d2d2 50%,#3a3a3a)"></div>
  <div class="info"><h3>Guido Vanderhoven</h3><div class="dates">12 June 1955 - 05 April 2019</div><div class="btn-gold download">Download Funeral letter</div><div class="btn-gold flowers">Order Flowers</div></div>
  <div class="form"><div class="field">Guido Vanderhoven</div><div class="field">Your name*</div><div class="field area">Leave a message*</div><div class="btn-gold send">Send</div></div>
</div>

<div class="btn-gold load-more">Load More</div>

<section class="cta" role="img" aria-label="Dark background photo with red flowers">
  <h2>Do You Have Any Questions Or Would You Like To Call In Our<br>Funeral Home? Contact Us. We Are Here For You.</h2>
  <div class="call">Call Now : 011 23 45 67</div>
  <div class="btn-gold">Contact Us Today</div>
</section>

<footer class="footer">
  <h4 style="left:142px">Quick Links</h4>
  <ul class="links" style="left:142px">
    <li>Home</li><li>About us</li><li>Condole online</li><li>Order flowers</li><li>Contact</li>
  </ul>
  <h4 style="left:310px">Contact Details</h4>
  <ul class="contact" style="left:310px">
    <li><svg width="12" height="16" viewBox="0 0 12 16"><path d="M6 0a6 6 0 0 0-6 6c0 4.5 6 10 6 10s6-5.5 6-10a6 6 0 0 0-6-6zm0 8.5A2.5 2.5 0 1 1 6 3.5a2.5 2.5 0 0 1 0 5z" fill="#222"/></svg><span>Funeral Home Delvoort<br>Lindeweg 14, 2490 Heidebeek (Valkendaal)</span></li>
    <li><svg width="12" height="12" viewBox="0 0 24 24"><path d="M5 2h5l2 6-3 2a12 12 0 0 0 5 5l2-3 6 2v5a2 2 0 0 1-2 2A18 18 0 0 1 3 4a2 2 0 0 1 2-2z" fill="#222"/></svg><span>011 23 45 67</span></li>
    <li><svg width="12" height="12" viewBox="0 0 24 24"><rect x="6" y="1" width="12" height="7" fill="none" stroke="#222" stroke-width="2"/><rect x="1" y="8" width="22" height="10" fill="#222"/><rect x="6" y="14" width="12" height="9" fill="#fff" stroke="#222" stroke-width="2"/></svg><span>011 23 45 67</span></li>
    <li><svg width="14" height="12" viewBox="0 0 24 18"><rect x="1" y="1" width="22" height="16" fill="none" stroke="#222" stroke-width="2"/><path d="M1 1l11 9 11-9" fill="none" stroke="#222" stroke-width="2"/></svg><span style="font-size:11px">mourningcenter.delvoort@example.com</span></li>
  </ul>
  <h4 style="left:596px">Location Map</h4>
  <div class="map" role="img" aria-label="Small street map showing the location of the funeral home"></div>
  <div class="brand"><span class="dot"></span><div class="name">Funeral home<br>Delvoort <small>bvba</small></div></div>
  <div class="social">
    <span style="background:#3b5998"></span><span style="background:#1da1f2"></span><span style="background:#0077b5"></span><span style="background:#a0715a"></span>
  </div>
</footer>

<div class="bottombar">
  <span class="l">Copyright © 2019 Funeral Home Delvoort. All Rights Reserved.</span>
  <span class="r">Sitemap &nbsp; | &nbsp; Privacy Policy</span>
</div>

</body>
</html>
```